New web design needed for our company

We need our website designing, it needs to be professional and look creative,
We are a plumbing and heating company called Kestrel Bay's (www.kestrelbays.co.uk)
I like this site design also some of the following maybe:
https://www.marnockheating.com/
http://www.tavelpower.co.uk

Please let me know when you want our logo files as it wont let me upload them

The design will require coding once the design is complete, i havent paid for this yet as i want to be sure the design is good before i commit.

The template needs to look professional and look like one of the leading companies.
The site will consist of all the features this site has https://www.marnockheating.com/

I like a modern design with the latest technology.

Must have a customer login page and a my account area

Target Market(s)

Everyone

Industry/Entity Type

Plumbing

Coding

Coded - Design and coding required

Number of Pages Required

5+ page

Font styles to use
Other font styles liked:
• whatever suites

Requirements
Must have
• The design will require coding once the design is complete, i havent paid for this yet as i want to be sure the design is good before i commit.
• The template needs to look professional and look like one of the leading companies.
• The site will consist of all the features this site has https://www.marnockheating.com/
• I like a modern design with the latest technology.
• Must have a customer login page and a my account area
Nice to have
• inspirational and different
Should not have
• plain boring designs like most plumbing websites, needs to be inspiring and attract people from first sight.

```html
<!DOCTYPE html>
<html lang="en">
<head>
<meta charset="utf-8">
<title>Kestrel Bay's – Plumbing &amp; Heating</title>
<link href="https://fonts.googleapis.com/css2?family=Kanit:wght@400;500;600&family=Open+Sans:wght@400;600&family=Raleway:wght@500;600;700&display=swap" rel="stylesheet">
<style>
:root{
  --navy:#153a86;
  --navy-deep:#0f2d6b;
  --coral:#f35b45;
  --coral-soft:#e9675a;
  --ink:#1a1a1a;
  --body:#4a4a4a;
  --muted:#9a9a9a;
  --dark:#232323;
  --white:#ffffff;
  --line:#e4e4e4;
}
*{box-sizing:border-box;margin:0;padding:0}
html,body{width:1200px;height:3203px;overflow:hidden}
body{position:relative;background:var(--white);font-family:"Open Sans",Arial,sans-serif;color:var(--body)}
.abs{position:absolute}
.photo{position:absolute}

/* header */
.site-header{position:absolute;left:0;top:0;width:1200px;height:117px;background:rgba(255,255,255,.72);z-index:3}
.brand{position:absolute;left:60px;top:30px;font-family:"Kanit",sans-serif;font-weight:600;font-size:42px;color:var(--navy);line-height:1}
.brand-sub{position:absolute;left:62px;top:78px;font-size:12px;color:var(--navy)}
.nav{position:absolute;right:60px;top:50px;display:flex;gap:34px;font-family:"Raleway",sans-serif;font-weight:700;font-size:17px;color:var(--ink);list-style:none}

/* hero */
.hero{position:absolute;left:0;top:0;width:1200px;height:604px;overflow:hidden}
.hero-photo{left:0;top:0;width:1200px;height:604px;background:linear-gradient(120deg,#6d6f74,#9a9b9f 40%,#c9c8c6 70%)}
.hero-shapes{position:absolute;left:0;top:0}
.hero-kicker{position:absolute;left:60px;top:322px;font-family:"Kanit",sans-serif;font-size:32px;color:var(--white);z-index:2}
.hero-title{position:absolute;left:60px;top:366px;font-family:"Kanit",sans-serif;font-weight:600;font-size:42px;color:var(--coral);letter-spacing:.5px;z-index:2}

/* about */
.about-title{position:absolute;left:64px;top:674px;font-family:"Kanit",sans-serif;font-weight:600;font-size:38px;color:var(--ink)}
.about-title span{color:var(--navy)}
.about-text{position:absolute;left:62px;top:748px;width:610px;font-size:13.4px;line-height:23px}
.about-text p{margin-bottom:21px}
.btn{position:absolute;left:60px;top:1101px;width:182px;height:46px;background:var(--coral);color:var(--white);font-family:"Raleway",sans-serif;font-weight:600;font-size:18px;display:flex;align-items:center;justify-content:center;border-radius:2px}
.about-frame{left:747px;top:747px;width:395px;height:289px;border:3px solid var(--coral);background:linear-gradient(135deg,#4d74b6,#8fb0d8)}
.about-worker{left:700px;top:860px;width:200px;height:293px;background:linear-gradient(180deg,#b9a28c,#6d86a8 45%,#4f6a93);border-radius:90px 90px 20px 20px}

/* offer */
.offer{position:absolute;left:0;top:1275px;width:1200px;height:582px;background:linear-gradient(120deg,#2b2b2b,#3d3d3d 60%,#2a2a2a);overflow:hidden}
.section-title{position:absolute;left:0;width:1200px;text-align:center;font-family:"Kanit",sans-serif;font-weight:600;font-size:36px;display:flex;align-items:center;justify-content:center;gap:12px}
.mark{width:22px;height:22px;border-radius:50%;background:var(--coral);display:inline-block}
.offer .section-title{top:64px;color:var(--white)}
.service{position:absolute;width:360px}
.service h3{font-family:"Raleway",sans-serif;font-weight:500;font-size:24px;color:var(--white);margin-bottom:8px}
.service p{font-size:12.8px;line-height:19px;color:#e6e6e6;width:260px}
.diamond{position:absolute;width:92px;height:92px;background:var(--coral);transform:rotate(45deg)}
.diamond-icon{position:absolute;width:60px;height:60px}

/* blog */
.blog .section-title{top:1940px;color:var(--ink)}
.post{position:absolute;width:342px}
.post-image{width:342px;height:196px}
.post h4{font-family:"Raleway",sans-serif;font-weight:700;font-size:16.5px;line-height:23px;color:var(--ink);margin-top:22px}
.post p{font-size:13px;line-height:20px;color:var(--muted);margin-top:10px}
.post-meta{border-top:1px solid var(--line);margin-top:14px;padding-top:14px;font-size:11.5px;color:#b4b4b4;display:flex;gap:18px}
.post-meta span::before{content:"";display:inline-block;width:11px;height:11px;border-radius:50%;background:var(--coral);margin-right:6px;vertical-align:-1px}
.sidebar{position:absolute;left:798px;top:2067px;width:342px;height:420px;border:1px solid var(--line)}
.side-item{padding:20px 30px 18px;border-bottom:1px solid var(--line)}
.side-item h5{font-family:"Raleway",sans-serif;font-weight:700;font-size:16px;line-height:23px;color:var(--ink)}
.side-item small{display:block;margin-top:10px;font-size:12px;color:var(--muted)}
.side-more{padding:12px 20px;font-family:"Raleway",sans-serif;font-size:21px;color:var(--coral)}

/* footer */
.footer{position:absolute;left:0;top:2590px;width:1200px;height:613px;background:var(--navy);overflow:hidden}
.footer-photo{left:0;top:0;width:1200px;height:130px;background:linear-gradient(90deg,#c5ccd8,#e8ecf2 40%,#8ea0c0)}
.contact-box{position:absolute;top:19px;width:331px;height:85px;background:var(--coral-soft);color:var(--white)}
.contact-box .ico{position:absolute;left:0;top:0;width:88px;height:85px;background:var(--coral);display:flex;align-items:center;justify-content:center}
.contact-box b{position:absolute;left:100px;top:20px;font-family:"Raleway",sans-serif;font-size:17px}
.contact-box span{position:absolute;left:100px;top:46px;font-size:13px}
.footer h6{position:absolute;font-family:"Raleway",sans-serif;font-weight:600;font-size:25px;color:var(--white)}
.footer-about{position:absolute;left:60px;top:252px;width:420px;font-size:12.6px;line-height:24px;color:var(--white)}
.links{position:absolute;list-style:none;font-size:12.6px;color:var(--white)}
.links li{height:32px}
.links li::before{content:"";display:inline-block;width:5px;height:5px;border-radius:50%;background:var(--coral);margin-right:12px;vertical-align:2px}
.footer-brand{position:absolute;left:843px;top:276px;font-family:"Kanit",sans-serif;font-weight:600;font-size:44px;color:var(--white)}
.newsletter{position:absolute;left:60px;top:463px;width:1080px;height:90px;background:var(--coral-soft);color:var(--white);font-size:18px;line-height:27px;padding:18px 20px}
.newsletter .field{position:absolute;left:582px;top:24px;width:345px;height:42px;background:var(--white)}
.newsletter .submit{position:absolute;left:927px;top:24px;width:133px;height:42px;background:#1e1e1e;font-family:"Raleway",sans-serif;font-weight:700;font-size:15px;display:flex;align-items:center;justify-content:center}
.copyright{position:absolute;left:0;top:578px;width:1200px;text-align:center;font-size:13px;color:var(--white)}
</style>
</head>
<body>

<section class="hero">
  <div class="photo hero-photo" role="img" aria-label="Plumber tightening a pipe joint with a red wrench under a sink"></div>
  <svg class="hero-shapes" width="1200" height="604" viewBox="0 0 1200 604">
    <polygon points="780,117 1200,117 1200,604 930,604 650,330" fill="#153a86"/>
    <polyline points="860,80 660,300 860,520" fill="none" stroke="#f35b45" stroke-width="5"/>
    <polyline points="820,220 735,300 820,380" fill="none" stroke="#ffffff" stroke-width="16"/>
    <polygon points="1200,220 1120,300 1200,380" fill="#8e8e94"/>
  </svg>
  <p class="hero-kicker">Contact our friendly team</p>
  <h1 class="hero-title">PLUMBING PROFESSIONALS</h1>
</section>

<header class="site-header">
  <div class="brand">Kestrel Bay's</div>
  <div class="brand-sub">Your Local Experts</div>
  <ul class="nav"><li>HOME</li><li>ABOUT US</li><li>SERVICES</li><li>WORK LOCATIONS</li><li>NEWS</li><li>CONTACT US</li></ul>
</header>

<section class="about">
  <h2 class="about-title">ABOUT <span>Kestrel Bay's</span></h2>
  <div class="about-text">
    <p>Lorem ipsum dolor sit amet, consectetur adipiscing elit, sed do eiusmod tempor incididunt ut labore et dolore magna aliqua. Ut enim ad minim veniam, quis nostrud exercitation. Lorem ipsum dolor sit amet, consectetur adipiscing elit, sed do eiusmod tempor incididunt ut labore et dolore magna aliqua. Ut enim ad minim veniam, quis nostrud exercitation.</p>
    <p>Lorem ipsum dolor sit amet, consectetur adipiscing elit, sed do eiusmod tempor incididunt ut labore et dolore magna aliqua. Ut enim ad minim veniam, quis nostrud exercitation.</p>
    <p>Lorem ipsum dolor sit amet, consectetur adipiscing elit, sed do eiusmod tempor incididunt ut labore et dolore magna aliqua. Ut enim ad minim veniam, quis nostrud exercitation. Lorem ipsum dolor sit amet, consectetur adipiscing elit, sed do eiusmod tempor incididunt ut labore et dolore magna aliqua. Ut enim ad minim veniam, quis nostrud exercitation. Lorem ipsum dolor sit amet, consectetur adipiscing elit, sed do eiusmod tempor incididunt ut labore et dolore magna aliqua. Ut enim ad minim veniam, quis nostrud exercitation.</p>
  </div>
  <div class="btn">Contact us today</div>
  <div class="photo about-frame" role="img" aria-label="Plumber working on pipes beneath a bathroom sink"></div>
  <div class="photo about-worker" role="img" aria-label="Smiling plumber crouching with a tool belt and notepad"></div>
</section>

<section class="offer">
  <svg class="abs" style="left:0;top:0" width="240" height="230" viewBox="0 0 240 230">
    <polygon points="0,0 110,0 210,100 110,200 0,200" fill="#1447c2"/>
    <polygon points="0,40 40,80 0,120" fill="#1e1e1e"/>
    <polyline points="160,40 210,100 160,160" fill="none" stroke="#bfbfbf" stroke-width="6"/>
    <polyline points="150,60 185,100 150,140" fill="none" stroke="#ffffff" stroke-width="10"/>
  </svg>
  <h2 class="section-title"><span class="mark"></span>WHAT WE OFFER</h2>

  <div class="diamond" style="left:134px;top:186px"></div>
  <svg class="diamond-icon" style="left:150px;top:202px" viewBox="0 0 60 60" fill="none" stroke="#fff" stroke-width="2.5"><rect x="18" y="24" width="22" height="16"/><path d="M40 30h8v6h-8M24 24v-8h10v8M22 40v8h14v-8"/></svg>
  <div class="service" style="left:262px;top:186px"><h3>Repairing</h3><p>Lorem ipsum dolor sit amet, consectetur adipiscing elit, sed do eiusmod tempor incididunt ut labore et dolore magna</p></div>

  <div class="diamond" style="left:659px;top:186px"></div>
  <svg class="diamond-icon" style="left:675px;top:202px" viewBox="0 0 60 60" fill="none" stroke="#fff" stroke-width="2.5"><path d="M16 44L40 20M38 14a7 7 0 0 0 8 8l-4 4-8-8zM16 16l28 28M14 20l6-6"/></svg>
  <div class="service" style="left:813px;top:186px"><h3>Expert and Profesional</h3><p>Lorem ipsum dolor sit amet, consectetur adipiscing elit, sed do eiusmod tempor incididunt ut labore et dolore magna</p></div>

  <div class="diamond" style="left:134px;top:419px"></div>
  <svg class="diamond-icon" style="left:150px;top:435px" viewBox="0 0 60 60" fill="none" stroke="#fff" stroke-width="2.5"><path d="M14 40a16 16 0 1 1 32 0"/><text x="22" y="38" font-size="11" fill="#fff" stroke="none" font-family="Arial">24</text><path d="M14 40h32v6H14z"/></svg>
  <div class="service" style="left:262px;top:365px"><h3>Expert and Profesional</h3><p>Lorem ipsum dolor sit amet, consectetur adipiscing elit, sed do eiusmod tempor incididunt ut labore et dolore magna</p></div>

  <div class="diamond" style="left:659px;top:419px"></div>
  <svg class="diamond-icon" style="left:675px;top:435px" viewBox="0 0 60 60" fill="none" stroke="#fff" stroke-width="2.5"><circle cx="30" cy="30" r="15"/><path d="M22 28h16l-8 8z"/></svg>
  <div class="service" style="left:809px;top:356px"><h3>24/7 Emergency Available</h3><p>Lorem ipsum dolor sit amet, consectetur adipiscing elit, sed do eiusmod tempor incididunt ut labore et dolore magna</p></div>
</section>

<section class="blog">
  <h2 class="section-title"><span class="mark"></span>LATEST BLOG</h2>
  <article class="post" style="left:60px;top:2067px">
    <div class="photo post-image" style="position:relative;background:linear-gradient(135deg,#3f68b3,#9bb4d6 60%,#e8e8e8)" role="img" aria-label="Plumber fixing pipework under a white basin"></div>
    <h4>The Importance Of Hiring Plumbers For Your Plumbing Fixes</h4>
    <p>Sed ut perspiciatis unde omnis iste natus error sit voluptatem accusa nt ium dolor emque laud adantium totam.</p>
    <div class="post-meta"><span>Rowan Hale</span><span>Comments: 6</span></div>
  </article>
  <article class="post" style="left:429px;top:2067px">
    <div class="photo post-image" style="position:relative;background:linear-gradient(135deg,#0d2340,#3f6f9c 55%,#b7cde0)" role="img" aria-label="Chrome tap running water into a sink"></div>
    <h4>How Plumbers Charge for Their Services : Asking the Right Questions</h4>
    <p>Sed ut perspiciatis unde omnis iste natus error sit voluptatem accusa nt ium dolor emque laud adantium totam.</p>
    <div class="post-meta"><span>Rowan Hale</span><span>Comments: 6</span></div>
  </article>
  <aside class="sidebar">
    <div class="side-item"><h5>Fenwick Plumbing nominated for Top Choice 2016</h5><small>5 days ago &nbsp;&nbsp; plumbing, repairs</small></div>
    <div class="side-item"><h5>Why Choose Only the Most Qualified Our Plumbers?</h5><small>5 days ago &nbsp;&nbsp; plumbing, repairs</small></div>
    <div class="side-item"><h5>Why is Timely Drain Cleaning Very Important for Homeowners?</h5><small>5 days ago &nbsp;&nbsp; plumbing, repairs</small></div>
    <div class="side-more">Read More</div>
  </aside>
</section>

<footer class="footer">
  <div class="photo footer-photo" role="img" aria-label="Plumber at work, faded behind the contact strip"></div>
  <div class="contact-box" style="left:60px"><div class="ico"><svg width="30" height="38" viewBox="0 0 30 38"><path d="M15 2a12 12 0 0 1 12 12c0 9-12 22-12 22S3 23 3 14A12 12 0 0 1 15 2z" fill="#fff"/><circle cx="15" cy="14" r="4.5" fill="#f35b45"/></svg></div><b>VISIT US:</b><span>12 Harbour Row, Kestrel Bay</span></div>
  <div class="contact-box" style="left:431px"><div class="ico"><svg width="36" height="26" viewBox="0 0 36 26"><rect x="1" y="1" width="34" height="24" fill="#fff"/><path d="M1 1l17 13L35 1" fill="none" stroke="#f35b45" stroke-width="2.5"/></svg></div><b>EMAIL US:</b><span>hello@kestrelbays.co.uk</span></div>
  <div class="contact-box" style="left:809px"><div class="ico"><svg width="32" height="32" viewBox="0 0 32 32"><path d="M7 2l6 7-3 4c2 4 5 7 9 9l4-3 7 6-4 5C14 30 2 18 2 6z" fill="#fff"/></svg></div><b>CALL US:</b><span>01632 960 418</span></div>

  <h6 style="left:60px;top:196px">About us</h6>
  <p class="footer-about">Lorem ipsum dolor sit amet, consectetur adipiscing elit, sed do eiusmod tempor incididunt ut labore et dolore magna ali qua. Lorem ipsum dolor sit amet, consectetur adipiscing. Lorem ipsum dolor sit amet, consectetur adipiscing elit, sed do eiusmod tempor incididunt ut labore et dolore magna ali qua. Lorem ipsum dolor sit amet, consectetur adipiscing elit.</p>
  <h6 style="left:485px;top:196px">Quick Links</h6>
  <ul class="links" style="left:487px;top:252px"><li>Drain Cleaning</li><li>Faucet Repairs</li><li>Sewer Cleaning</li><li>Heating &amp; Cooling</li><li>Water Treatment</li></ul>
  <h6 style="left:664px;top:196px">Services</h6>
  <ul class="links" style="left:666px;top:254px"><li>Drain Cleaning</li><li>Faucet Repairs</li><li>Sewer Cleaning</li><li>Heating &amp; Cooling</li><li>Water Treatment</li></ul>
  <div class="footer-brand">Kestrel Bay's</div>

  <div class="newsletter">Subscribe now and recive weekly newsletter with new<br>tips and exciting offers or discounts.
    <div class="field"></div><div class="submit">SUBSCRIBE</div>
  </div>
  <p class="copyright">Copyright © Kestrel Bay's 2016. All rights reserved.</p>
</footer>

</body>
</html>
```